The Timber Loft

We need a business card design for our wardrobe company.
Please visit our website www.zorvelcabinets.com to get an idea of who we are.

```html
<!DOCTYPE html>
<html lang="en">
<head>
<meta charset="utf-8">
<title>The Timber Loft – Business Card</title>
<link rel="stylesheet" href="https://fonts.googleapis.com/css2?family=Montserrat:wght@700&family=Open+Sans:wght@400;600&display=swap">
<style>
  :root {
    --backdrop: #e4e4e8;
    --card: #232323;
    --card-edge: #1b1b1b;
    --gold: #a8885a;
    --text-light: #e6e6e6;
    --text-muted: #9a9a9a;
    --white: #ffffff;
  }
  * { margin: 0; padding: 0; box-sizing: border-box; }
  html, body {
    width: 1200px;
    height: 1000px;
    overflow: hidden;
    background: var(--backdrop);
  }
  .stage {
    position: relative;
    width: 1200px;
    height: 1000px;
  }
  .business-card {
    position: absolute;
    left: 170px;
    top: 240px;
    width: 860px;
    height: 520px;
    background: var(--card);
    border: 1px solid var(--card-edge);
    box-shadow: 0 18px 40px rgba(0, 0, 0, 0.25);
    font-family: "Open Sans", sans-serif;
    color: var(--text-light);
  }
  .brand {
    position: absolute;
    left: 40px;
    top: 0;
    width: 330px;
    height: 100%;
    display: flex;
    flex-direction: column;
    justify-content: center;
    align-items: center;
    padding-top: 20px;
  }
  .brand-row {
    display: flex;
    align-items: center;
    gap: 14px;
  }
  .brand-square {
    width: 26px;
    height: 26px;
    border: 3px solid var(--white);
  }
  .brand-name {
    font-weight: 600;
    font-size: 27px;
    letter-spacing: 1px;
    color: var(--white);
    text-transform: uppercase;
  }
  .brand-tagline {
    margin-top: 10px;
    font-weight: 600;
    font-size: 19px;
    color: var(--white);
  }
  .divider {
    position: absolute;
    left: 390px;
    top: 90px;
    width: 1px;
    height: 310px;
    background: var(--gold);
  }
  .contact {
    position: absolute;
    left: 425px;
    top: 108px;
  }
  .person-name {
    font-family: "Montserrat", sans-serif;
    font-weight: 700;
    font-size: 36px;
    color: var(--gold);
    line-height: 1;
  }
  .person-role {
    margin-top: 6px;
    font-size: 13px;
    letter-spacing: 4px;
    color: var(--text-muted);
    text-transform: uppercase;
  }
  .contact-list {
    list-style: none;
    margin-top: 16px;
  }
  .contact-item {
    display: flex;
    align-items: flex-start;
    gap: 12px;
    font-size: 20px;
    line-height: 30px;
    color: var(--text-light);
  }
  .contact-icon {
    flex: 0 0 18px;
    width: 18px;
    height: 18px;
    margin-top: 6px;
    fill: var(--gold);
  }
</style>
</head>
<body>
  <main class="stage">
    <article class="business-card">
      <section class="brand">
        <div class="brand-row">
          <span class="brand-square"></span>
          <span class="brand-name">The Timber Loft</span>
        </div>
        <p class="brand-tagline">Fitted Right, Built True</p>
      </section>

      <div class="divider"></div>

      <section class="contact">
        <h1 class="person-name">Rowan Pike</h1>
        <p class="person-role">Director</p>
        <ul class="contact-list">
          <li class="contact-item">
            <svg class="contact-icon" viewBox="0 0 24 24" aria-hidden="true"><path d="M6.6 10.8a15.1 15.1 0 0 0 6.6 6.6l2.2-2.2a1 1 0 0 1 1-.25 11.4 11.4 0 0 0 3.6.57 1 1 0 0 1 1 1V20a1 1 0 0 1-1 1A17 17 0 0 1 3 4a1 1 0 0 1 1-1h3.5a1 1 0 0 1 1 1c0 1.25.2 2.45.57 3.6a1 1 0 0 1-.25 1z"/></svg>
            <span>0207 555 0148</span>
          </li>
          <li class="contact-item">
            <svg class="contact-icon" viewBox="0 0 24 24" aria-hidden="true"><path d="M3 5h18a1 1 0 0 1 1 1v12a1 1 0 0 1-1 1H3a1 1 0 0 1-1-1V6a1 1 0 0 1 1-1zm9 7.2L20 7H4z"/></svg>
            <span>info@zorvelcabinets.com</span>
          </li>
          <li class="contact-item">
            <svg class="contact-icon" viewBox="0 0 24 24" aria-hidden="true"><path d="M12 2a7 7 0 0 0-7 7c0 5.2 7 13 7 13s7-7.8 7-13a7 7 0 0 0-7-7zm0 9.5A2.5 2.5 0 1 1 12 6.5a2.5 2.5 0 0 1 0 5z"/></svg>
            <span>Alder House, 42 Mill Lane,<br>London N4 7QT</span>
          </li>
        </ul>
      </section>
    </article>
  </main>
</body>
</html>
```